AUSTRALIAN CONSULTING FIRM BUSINESS CARD - MODERN

We are wanting a modern, clean lined business card design. We are professional niche consultancy firm situated in Australia called Marlow Advisory Partners Pty Ltd.
The card should communicate professionalism and creativity and draw on our logo design (attached).
The design should be two sided, landscape orientation.
Target Market(s)
government, not for profit sector, corporate clients
Industry/Entity Type
Landscape
Requirements
Must have
- logo
no new introduced colours

```html
<!DOCTYPE html>
<html lang="en">
<head>
<meta charset="utf-8">
<title>Marlow Advisory Partners – Business Card</title>
<link rel="stylesheet" href="https://fonts.googleapis.com/css2?family=Arimo:wght@400;700&family=Roboto+Condensed:wght@700&display=swap">
<style>
  :root {
    --page: #ffffff;
    --card-front: #ffffff;
    --card-edge: #d9d9d9;
    --arc: #ececec;
    --brand-navy: #2b2a80;
    --brand-blue: #1a8fd6;
    --card-back: #f7c300;
    --ink: #15162a;
    --tag-red: #d8262d;
    --tag-bg: #ffffff;
  }
  * { box-sizing: border-box; margin: 0; padding: 0; }
  html, body {
    width: 1169px;
    height: 1200px;
    overflow: hidden;
    background: var(--page);
  }
  .sheet {
    position: relative;
    width: 1169px;
    height: 1200px;
  }
  .card {
    position: absolute;
    left: 224px;
    width: 779px;
    height: 418px;
    border-radius: 24px;
    overflow: hidden;
  }
  .card--front {
    top: 177px;
    background: var(--card-front);
    border: 1px solid var(--card-edge);
  }
  .card--back {
    top: 606px;
    background: var(--card-back);
  }
  .front-arcs {
    position: absolute;
    inset: 0;
  }
  .wordmark {
    position: absolute;
    left: 158px;
    top: 128px;
    display: flex;
    align-items: center;
    gap: 20px;
  }
  .wordmark__dot {
    width: 46px;
    height: 46px;
    border-radius: 50%;
    background: var(--brand-blue);
    flex: none;
  }
  .wordmark__text {
    font-family: "Arimo", Arial, sans-serif;
    font-weight: 700;
    color: var(--brand-navy);
    line-height: 1;
  }
  .wordmark__name {
    display: block;
    font-size: 66px;
    letter-spacing: -1px;
  }
  .wordmark__sub {
    display: block;
    font-size: 19px;
    margin-top: 8px;
    letter-spacing: 0.2px;
  }
  .notch {
    position: absolute;
    left: 432px;
    bottom: 0;
    width: 0;
    height: 0;
    border-left: 21px solid transparent;
    border-right: 21px solid transparent;
    border-bottom: 38px solid var(--page);
  }
  .company-name {
    position: absolute;
    left: 442px;
    top: 100px;
    font-family: "Roboto Condensed", "Arial Narrow", sans-serif;
    font-weight: 700;
    font-size: 27px;
    line-height: 36px;
    color: var(--ink);
  }
  .contact-list {
    position: absolute;
    left: 433px;
    top: 202px;
    list-style: none;
  }
  .contact-list li {
    display: flex;
    align-items: center;
    height: 37px;
    font-family: "Arimo", Arial, sans-serif;
    font-size: 18px;
    color: var(--ink);
  }
  .contact-tag {
    width: 35px;
    height: 22px;
    margin-right: 12px;
    background: var(--tag-bg);
    border-bottom: 3px solid var(--tag-red);
    border-radius: 3px;
    color: var(--tag-red);
    font-size: 14px;
    line-height: 19px;
    text-align: center;
  }
</style>
</head>
<body>
<main class="sheet">
  <section class="card card--front" aria-label="Card front">
    <svg class="front-arcs" width="779" height="418" viewBox="0 0 779 418" aria-hidden="true">
      <path d="M233 430 Q260 150 440 -10" fill="none" stroke="var(--arc)" stroke-width="88"/>
      <path d="M372 430 Q480 180 800 135" fill="none" stroke="var(--arc)" stroke-width="88"/>
    </svg>
    <div class="wordmark">
      <span class="wordmark__dot"></span>
      <span class="wordmark__text">
        <span class="wordmark__name">MARLOW</span>
        <span class="wordmark__sub">ADVISORY PARTNERS PTY LTD</span>
      </span>
    </div>
  </section>

  <section class="card card--back" aria-label="Card back">
    <h1 class="company-name">Marlow Advisory<br>Partners Pty Ltd.</h1>
    <ul class="contact-list">
      <li><span class="contact-tag">p</span>02 5550 0142</li>
      <li><span class="contact-tag">e</span>hello@marlowadvisory.com.au</li>
      <li><span class="contact-tag">w</span>www.marlowadvisory.com.au</li>
    </ul>
    <span class="notch"></span>
  </section>
</main>
</body>
</html>
```